Business Card Design Project

TRK Solutions is a Electrical and Communications Services and Maintenance contractor to the Mining Oil and Gas sectors of Australia.
Our clients will be planners, Schedulers, Tradespeople and Engineers

We are yet to determine the primary colours that we will use on the business cards but the logos attached will form foundation of the colours used for logos on Business cards, Website, Uniforms, vehicles etc.

Target Market(s)

Mining engineers and shedulers

Industry/Entity Type

Contractor

Requirements
Must have
• information to be included on the card

Name: Derek Hanley
Title: Managing Director
Company: TRK Solutions Pty Ltd
Phone: 08 9YYY YYYY
Mobile 0400 813 942
email: dhanley@trksolutions-example.com
Website www.trksolutions-example.com

Address: U5/7 Bexley Street Malaga, WA 6090
Postal Address: PO Box 4187 Malaga WA 6944

Nice to have
• Double sided. Maybe the logo on the back

```html
<!DOCTYPE html>
<html lang="en">
<head>
<meta charset="utf-8">
<title>TRK Solutions – Business Card</title>
<link rel="stylesheet" href="https://fonts.googleapis.com/css2?family=Montserrat:wght@400;500;600&display=swap">
<style>
  :root {
    --page: #ffffff;
    --card: #1f2426;
    --card-light: #262c2e;
    --edge: #6a3a2e;
    --ink: #e6e8e8;
    --ink-soft: #b9bebf;
    --accent: #e2501f;
    --rule: #5a6163;
  }
  * { box-sizing: border-box; margin: 0; padding: 0; }
  html, body {
    width: 1200px;
    height: 1128px;
    overflow: hidden;
    background: var(--page);
    font-family: "Montserrat", sans-serif;
  }
  .card {
    position: absolute;
    left: 453px;
    width: 392px;
    height: 226px;
    border-radius: 26px;
    background: linear-gradient(135deg, var(--card-light), var(--card) 60%);
    box-shadow: 0 0 0 1px var(--edge);
    color: var(--ink);
    overflow: hidden;
  }
  .card--front { top: 291px; }
  .card--back  { top: 614px; }

  .brand {
    position: absolute;
    left: 50px;
    top: 60px;
    display: flex;
    align-items: center;
    gap: 8px;
  }
  .brand__name {
    font-size: 26px;
    font-weight: 400;
    letter-spacing: 0.3px;
    color: var(--ink);
    white-space: nowrap;
  }
  .brand__mark {
    width: 9px;
    height: 9px;
    background: var(--accent);
  }

  .person {
    position: absolute;
    right: 175px;
    top: 177px;
    text-align: right;
    font-size: 6.5px;
    line-height: 10px;
    white-space: nowrap;
  }
  .person__name { font-weight: 600; color: var(--ink); }
  .person__title { color: var(--ink-soft); }

  .divider {
    position: absolute;
    left: 224px;
    top: 157px;
    width: 1px;
    height: 41px;
    background: var(--rule);
  }

  .contact {
    position: absolute;
    left: 256px;
    top: 159px;
    font-size: 6px;
    line-height: 9px;
    color: var(--ink-soft);
    white-space: nowrap;
  }
  .contact__company { font-weight: 600; color: var(--ink); }
  .contact__web { color: var(--accent); letter-spacing: 0.4px; font-weight: 500; }

  .address {
    position: absolute;
    left: 156px;
    top: 174px;
    display: flex;
    align-items: center;
    gap: 8px;
  }
  .address__mark {
    width: 12px;
    height: 17px;
    border: 1px solid var(--ink-soft);
    border-radius: 3px;
  }
  .address__lines {
    font-size: 6px;
    line-height: 9px;
    color: var(--ink-soft);
    white-space: nowrap;
  }
</style>
</head>
<body>
  <section class="card card--front" aria-label="Business card front">
    <div class="brand">
      <span class="brand__name">TRK Solutions</span>
      <span class="brand__mark"></span>
    </div>
    <div class="person">
      <p class="person__name">Derek Hanley</p>
      <p class="person__title">Managing Director</p>
    </div>
    <div class="divider"></div>
    <div class="contact">
      <p class="contact__company">TRK Solutions Pty Ltd</p>
      <p>P 08 9YYY YYYY &nbsp;M 0400 813 942</p>
      <p>dhanley@trksolutions-example.com</p>
      <p class="contact__web">www.trksolutions-example.com</p>
    </div>
  </section>

  <section class="card card--back" aria-label="Business card back">
    <div class="address">
      <span class="address__mark"></span>
      <div class="address__lines">
        <p>Address: U5/7 Bexley Street Harlow Ridge, KR 4410</p>
        <p>Postal Address: PO Box 4187 Harlow Ridge KR 4419</p>
      </div>
    </div>
  </section>
</body>
</html>
```